Soho based IT support firm flyer.

We need a flyer to boost our business. We're a tech support firm based in Soho, London and provide helpdesk and call out support to SMEs in and around London.
They'll be two flyers with the same design. One is location specific and has the copy:
-
1 Month Free IT Support!
Based in Soho, we provide expert tech support for both Zelks and PCs.
We have monthly as well as pay-as-you-go plans to fit your business.
Call us now and we'll show you how we can save you up to 50% on your IT spend.
-None location based is-
1 Month Free IT Support!
We provide expert, professional tech support for both Zelks and PCs.
• Dedicated full time helpdesk
• Same day onsite visits
• Proactive support with monitoring
• 98% satisfaction score*
*taken from satisfaction survey sent out on closure of every case for Oct 2011 to Oct 2012
-
The location one needs to include a map with our location marked as postcode Q9X 4TT.
I'm fine with royalty photos being used within a reasonable price. Please use PicturVault.
Our site shows our brand best. Please keep as close to this as possible.
http://brivo-desk.example
Thanks for looking.

```html
<!DOCTYPE html>
<html lang="en">
<head>
<meta charset="utf-8">
<title>Brivo Desk – Location Specific Flyer</title>
<link rel="stylesheet" href="https://fonts.googleapis.com/css2?family=Josefin+Sans:wght@600;700&family=Poiret+One&family=Yanone+Kaffeesatz:wght@300&display=swap">
<style>
  :root {
    --leaf-green: #5e9111;
    --lime: #b6d90f;
    --band-yellow: #d6e21a;
    --band-orange: #f29a1e;
    --charcoal: #333333;
    --box-text: #e4e4e4;
    --ink: #1f2b0b;
    --pale: #eef5d6;
    --white: #ffffff;
    --phone-orange: #f08a1e;
    --map-green: #54830e;
    --bark-dark: #3a332c;
    --bark-mid: #6e655a;
    --bark-light: #948a7c;
  }
  * { margin: 0; padding: 0; box-sizing: border-box; }
  html, body { width: 1200px; height: 1000px; overflow: hidden; background: var(--leaf-green); }
  .flyer { position: relative; width: 1200px; height: 1000px; background: var(--leaf-green); font-family: "Yanone Kaffeesatz", sans-serif; }

  .brand { position: absolute; left: 86px; top: 30px; display: flex; align-items: center; gap: 10px;
    font-family: "Josefin Sans", sans-serif; font-weight: 700; font-size: 38px; color: var(--lime); }
  .brand-dot { width: 16px; height: 16px; border-radius: 50%; background: var(--lime); }

  .header-rule { position: absolute; left: 0; top: 92px; width: 1200px; height: 12px;
    background: linear-gradient(var(--band-yellow) 0 60%, var(--band-orange) 60% 100%); }

  .label-box { position: absolute; background: var(--charcoal); color: var(--box-text);
    font-family: "Poiret One", sans-serif; line-height: 1; box-shadow: 3px 3px 6px rgba(0,0,0,.35);
    display: flex; align-items: center; padding-left: 8px; }
  .label-location { left: 10px; top: 155px; width: 460px; height: 60px; font-size: 50px; letter-spacing: 1px; }
  .label-phone { left: 724px; top: 186px; width: 160px; height: 46px; font-size: 44px; }
  .label-email { left: 726px; top: 245px; width: 136px; height: 55px; font-size: 44px; }

  .offer-title { position: absolute; left: 25px; top: 232px; font-family: "Josefin Sans", sans-serif;
    font-weight: 700; font-size: 28px; color: var(--white); }
  .offer-copy { position: absolute; left: 25px; top: 268px; font-weight: 300; font-size: 28px;
    line-height: 36.8px; color: var(--ink); }
  .offer-copy .pale { color: var(--pale); }
  .offer-copy .pale .ink { color: var(--ink); }

  .call-line { position: absolute; left: 727px; top: 110px; font-weight: 300; font-size: 28px;
    line-height: 36px; color: var(--ink); }
  .call-line .highlight { color: var(--pale); }

  .phone-number { position: absolute; left: 899px; top: 194px; font-family: "Josefin Sans", sans-serif;
    font-weight: 700; font-size: 31px; letter-spacing: 2px; color: var(--phone-orange); }
  .email-address { position: absolute; left: 901px; top: 258px; font-family: "Josefin Sans", sans-serif;
    font-weight: 700; font-size: 28px; color: var(--white); }

  .location-map { position: absolute; left: 660px; top: 375px; width: 470px; height: 198px; background: var(--map-green); }

  .base-rule { position: absolute; left: 0; top: 574px; width: 1200px; height: 3px; background: var(--band-orange); }

  .bark-photo { position: absolute; left: 0; top: 577px; width: 1200px; height: 423px;
    background: linear-gradient(90deg, var(--bark-dark) 0%, var(--bark-mid) 18%, var(--bark-dark) 32%, var(--bark-light) 48%, var(--bark-dark) 60%, var(--bark-mid) 75%, var(--bark-dark) 88%, var(--bark-mid) 100%); }
</style>
</head>
<body>
<div class="flyer">
  <div class="brand"><span>Brivo Desk</span><span class="brand-dot"></span></div>
  <div class="header-rule"></div>

  <div class="label-box label-location">LOCATION SPECIFIC</div>
  <h1 class="offer-title">1 Month Free IT Support!</h1>
  <p class="offer-copy">
    Based in Soho<br>
    We provide<br>
    expert, professional tech support for both<br>
    Zelks and PCs<br>
    <span class="pale">We have monthly as well as <span class="ink">pay-as-you-go</span> plans to fit<br>
    your business</span>
  </p>

  <p class="call-line">Call us now and we'll show you how we<br>can save you up to <span class="highlight">50%</span> on your IT spend</p>
  <div class="label-box label-phone">PHONE</div>
  <div class="phone-number">0207 946 0831</div>
  <div class="label-box label-email">EMAIL</div>
  <div class="email-address">info@brivo-desk.example</div>

  <div class="location-map" role="img" aria-label="Street map of Soho around Oxford Street and New Oxford Street, marking the office at postcode Q9X 4TT"></div>
  <div class="base-rule"></div>
  <div class="bark-photo" role="img" aria-label="Close-up photograph of weathered tree bark with moss"></div>
</div>
</body>
</html>
```